Zielgruppe
Ich bin Selfpublisher und habe eine Lust Wunschzettel als Buch kreiert. Die Zielgruppe sind meist junge Erwachsene, aber auch welche mittleren alters.
Aufgabenstellung
Titel des Buches: Der dicke LUST WUNSCHZETTEL
Untertitel: 150 Orte +10 eigene Orte für mehr Nervenkitzel und Erlebnisse
Der Anfang vom Titel 'Der dicke' kann ruhig sehr klein abgebildet werden.
Das Wort 'SEX' im Titel soll am größten auf dem Cover sein und auch bei kleinster Darstellung gut sichtbar und sehr prägnant sein.
Der Teil vom Untertitel '+10 eigene Orte für mehr Nervenkitzel und Erlebnisse' kann ruhig getrennt von den '150 Orten' stehen.
In dem Buch sind 150 Orte plus jeweils Felder zum Ankreuzen und beschreiben vorhanden, wie der Sex dort war.
Farben: Die Hauptfarbe soll ins rote gehen.
Auf keinen Fall darf dieses Rot #EE3A43 benutzt werden, da dies die Farbe eines Mitbewerbers ist.
Hier zwei Beispiele welche Farben benutzt werden können: #FF4D8D, #FF6686. Natürlich sind auch andere und ähnliche Farben in Ordnung. Dies diente nur zur Orientierung, wie weit das Rot verändert werden muss.
Es sollen keine echten Fotos verwendet werden. Außerdem sollen keine Menschen, oder Illustrationen von Menschen abgebildet werden.
Ich habe eine Datei hochgeladen, worin sich mehrere Illustrationen befinden. Die können in der Farbe und vom Aussehen verändert werden. Das benutzen der Illustrationen ist absolut kein muss! Ich lasse mich gerne von anderen Designs überraschen.
Mit den Illustrationen könnte man zum Beispiel sowas wie auf dem Cover der 'Onkel Tourenheft' abgebildet machen. Bild ist im Anhang. Hierfür müssen die Illustrationen (Sex Icons) mit passenden Farben versehen werden. Es sollte nicht zu Bunt werden, also hier 3-4 Farben aussuchen.
Außerdem eventuell ein Schrift Effekt wie bei dem Titel der 'Garden Quest' auch im Anhang zu finden. Natürlich gehen auch andere passende Effekte. Hier kenne ich mich nicht aus, was so möglich ist.
Es sollte allgemein nicht zu langweilig sein. Etwas Dynamik und Effekte sind gut. Wie bei den bereits genannten Beispiel Covern.

```html
<!DOCTYPE html>
<html lang="de">
<head>
<meta charset="utf-8">
<title>Der dicke Lust Wunschzettel – Buchcover</title>
<link rel="stylesheet" href="https://fonts.googleapis.com/css2?family=Archivo+Black&family=Poppins:wght@800&display=swap">
<style>
  :root {
    --stage: #f5f5f5;
    --rose: #ec6480;
    --rose-shade: #b0485c;
    --plum: #4a1a2e;
    --paper: #ffffff;
    --curl-grey: #b5b5b5;
    --curl-light: #dedede;
  }
  html, body {
    margin: 0;
    width: 1200px;
    height: 1200px;
    overflow: hidden;
    background: var(--stage);
  }
  .book-cover {
    position: absolute;
    left: 220px;
    top: 30px;
    width: 760px;
    height: 1140px;
    display: block;
  }
  .title-display {
    font-family: "Archivo Black", "Arial Black", sans-serif;
  }
  .title-prefix {
    font-family: "Poppins", "Arial", sans-serif;
    font-weight: 800;
  }
  .subline {
    font-family: "Poppins", "Arial", sans-serif;
    font-weight: 800;
    fill: var(--rose);
  }
</style>
</head>
<body>
<svg class="book-cover" viewBox="0 0 968 1452" xmlns="http://www.w3.org/2000/svg" aria-label="Buchcover Der dicke Lust Wunschzettel">
  <rect class="cover-paper" x="0" y="0" width="968" height="1452" fill="var(--paper)"/>
  <rect class="cover-field" x="0" y="0" width="968" height="1304" fill="var(--rose)"/>

  <g class="speech-bubble">
    <path class="speech-bubble__shadow" fill="var(--rose-shade)"
      d="M118 191 L792 141 Q833 141 833 175 L833 482 Q833 512 797 516 L708 524 L635 590 L635 533 L127 580 Q86 580 86 546 L86 220 Q86 193 118 191 Z"/>
    <path class="speech-bubble__body" fill="var(--paper)"
      d="M143 161 L817 111 Q858 111 858 145 L858 452 Q858 482 822 486 L724 494 L615 584 L615 503 L152 543 Q111 543 111 510 L111 190 Q111 163 143 161 Z"/>
    <g class="speech-bubble__title" fill="var(--rose)" transform="rotate(-5 470 340)">
      <text class="title-prefix" x="180" y="238" font-size="42"
        textLength="210" lengthAdjust="spacingAndGlyphs">Der dicke</text>
      <text class="title-display" x="172" y="462" font-size="260"
        textLength="610" lengthAdjust="spacingAndGlyphs">LUST</text>
    </g>
  </g>

  <g class="main-title" fill="var(--paper)">
    <text class="title-display" x="145" y="772" font-size="170"
      textLength="681" lengthAdjust="spacingAndGlyphs">WUNSCH</text>
    <text class="title-display" x="145" y="952" font-size="170"
      textLength="400" lengthAdjust="spacingAndGlyphs">ZETTEL</text>
  </g>

  <g class="return-arrow">
    <path fill="var(--rose-shade)" transform="translate(8 4)"
      d="M565 856 L670 880 L648 903 Q700 940 760 915 Q800 880 773 834 Q790 890 760 930 Q700 980 620 936 L597 959 Z"/>
    <path fill="var(--paper)"
      d="M565 856 L670 880 L648 903 Q700 940 760 915 Q800 880 773 834 Q790 890 760 930 Q700 980 620 936 L597 959 Z"/>
  </g>

  <g class="places-count">
    <rect x="145" y="1009" width="250" height="165" rx="20" fill="var(--plum)"/>
    <text class="title-display" x="160" y="1155" font-size="180"
      textLength="218" lengthAdjust="spacingAndGlyphs" fill="var(--rose)">150</text>
    <ellipse cx="474" cy="1158" rx="46" ry="10" fill="var(--rose-shade)"/>
    <path class="pin-icon" fill="var(--paper)" fill-rule="evenodd"
      d="M474 1025 a45 45 0 1 1 -0.1 0 Z M474 1048 a22 22 0 1 0 0.1 0 Z M450 1121 Q474 1130 498 1121 L478 1154 Q474 1160 470 1154 Z"/>
    <text class="title-display" x="535" y="1155" font-size="180"
      textLength="241" lengthAdjust="spacingAndGlyphs" fill="var(--paper)">RTE</text>
  </g>

  <g class="page-curl">
    <path fill="var(--paper)"
      d="M968 958 C920 1150 800 1240 633 1232 C740 1270 790 1340 760 1452 L968 1452 Z"/>
    <path fill="var(--rose-shade)"
      d="M633 1232 C700 1248 750 1272 775 1304 L738 1304 C712 1272 675 1250 633 1232 Z"/>
    <path fill="var(--curl-grey)"
      d="M738 1304 L775 1304 C810 1345 805 1395 760 1452 C770 1395 765 1345 738 1304 Z"/>
    <path fill="var(--curl-light)"
      d="M962 1098 C945 1250 890 1380 780 1446 C870 1360 930 1250 962 1098 Z"/>
  </g>

  <g class="subline">
    <text x="145" y="1353" font-size="36" textLength="510" lengthAdjust="spacingAndGlyphs">+10 EIGENE ORTE FÜR MEHR</text>
    <text x="145" y="1408" font-size="36" textLength="597" lengthAdjust="spacingAndGlyphs">NERVENKITZEL UND ERLEBNISSE</text>
  </g>
</svg>
</body>
</html>
```